Youth deer hunt give away flyer.

We need a flyer designed for a youth deer hunt giveaway that we are doing. We are an Illinois whitetail deer hunting outfitter. We house and feed our clients as well as providing them with a guided deer hunt. It needs to include images as well as details about the giveaway. Im looking for a proffesional, looking flyer

Target Market(s)

rednecks, hunters

Industry/Entity Type

Hunting

Font styles to use
Serif
Sans Serif

Colors
000000
dbdbdb
ffffff
474747

Requirements
Must have
• not sure
Nice to have
• not sure
Should not have
• not sure

```html
<!DOCTYPE html>
<html lang="en">
<head>
<meta charset="utf-8">
<title>Harlan Ridge Outfitting – 2018 Youth Firearm Hunt</title>
<link rel="stylesheet" href="https://fonts.googleapis.com/css2?family=Roboto+Slab:wght@700;900&family=Open+Sans:wght@400;600;700;800&family=PT+Sans+Narrow:wght@400;700&display=swap">
<style>
  :root {
    --black: #000000;
    --panel-grey: #dbdbdb;
    --white: #ffffff;
    --charcoal: #474747;
    --hunt-orange: #e0472a;
    --band-orange: #c8401f;
    --wood-dark: #2f2620;
    --wood-mid: #4a3b31;
    --wood-light: #5c4a3d;
  }
  * { margin: 0; padding: 0; box-sizing: border-box; }
  html, body { width: 927px; height: 1200px; overflow: hidden; background: var(--white); }
  .flyer { position: relative; width: 927px; height: 1200px; overflow: hidden; font-family: "Open Sans", Arial, sans-serif; }

  .hero-photo {
    position: absolute; left: 0; top: 0; width: 927px; height: 600px;
    background: radial-gradient(ellipse at 35% 70%, #b79b7d 0%, #8a725c 35%, #2a2622 70%, #0b0b0b 100%);
  }
  .title-panel { position: absolute; left: 487px; top: 0; width: 440px; height: 600px; }
  .title-panel svg { position: absolute; inset: 0; }

  .brand-mark { position: absolute; left: 683px; top: 140px; width: 44px; height: 44px; border-radius: 50%; background: var(--charcoal); }
  .brand-name, .brand-sub { position: absolute; left: 487px; width: 440px; text-align: center; color: var(--charcoal); font-family: "Roboto Slab", Rockwell, Georgia, serif; font-weight: 700; white-space: nowrap; }
  .brand-name { top: 210px; font-size: 34px; line-height: 40px; letter-spacing: 1px; }
  .brand-sub { top: 252px; font-size: 14px; line-height: 18px; letter-spacing: 4px; }

  .headline { margin: 0; }
  .headline span { position: absolute; left: 487px; width: 440px; text-align: center; color: var(--hunt-orange); font-family: "Roboto Slab", Rockwell, Georgia, serif; font-weight: 900; white-space: nowrap; }
  .headline .year { top: 296px; font-size: 84px; line-height: 84px; }
  .headline .youth { top: 374px; font-size: 74px; line-height: 74px; }
  .headline .firearm { top: 442px; font-size: 54px; line-height: 58px; }
  .headline .hunt { top: 494px; font-size: 76px; line-height: 76px; }

  .contact-band { position: absolute; left: 0; top: 600px; width: 927px; height: 32px; background: var(--band-orange); color: var(--white); font-weight: 700; font-size: 18.5px; letter-spacing: .6px; text-align: center; line-height: 32px; white-space: nowrap; }

  .details { position: absolute; left: 0; top: 632px; width: 927px; height: 568px; background: repeating-linear-gradient(90deg, var(--wood-dark) 0 3px, var(--wood-mid) 3px 9px, var(--wood-light) 9px 11px, var(--wood-mid) 11px 17px); }

  .side-photo { position: absolute; left: 4px; width: 312px; }
  .photo-trophy { top: 640px; height: 166px; background: linear-gradient(135deg, #6b5132, #3e3424 60%, #7b6243); }
  .photo-interior { top: 818px; height: 204px; background: linear-gradient(180deg, #b08452, #8a5e34 60%, #5a4436); }
  .photo-cabin { top: 1030px; height: 170px; background: linear-gradient(180deg, #f2f2f2 0 30%, #c89a5b 30% 80%, #6f9a3f 80%); }

  .event-date { position: absolute; left: 340px; top: 640px; color: var(--white); font-family: "Roboto Slab", Rockwell, Georgia, serif; font-weight: 700; font-size: 50px; line-height: 60px; white-space: nowrap; }

  .package { position: absolute; left: 347px; top: 712px; list-style: none; color: var(--white); font-weight: 700; font-size: 18.5px; line-height: 1.3; }
  .package li { position: relative; padding-left: 24px; margin-bottom: 6px; white-space: nowrap; }
  .package li svg { position: absolute; left: 0; top: 7px; }

  .about { position: absolute; left: 342px; top: 866px; width: 564px; height: 152px; background: rgba(255,255,255,.14); border-radius: 8px; padding: 12px 14px; color: var(--white); font-family: "PT Sans Narrow", "Arial Narrow", sans-serif; font-size: 14px; line-height: 1.4; }
  .about p + p { margin-top: 8px; }

  .owner { position: absolute; left: 420px; top: 1070px; color: var(--white); font-style: normal; }
  .owner-name { font-weight: 700; font-size: 15px; letter-spacing: .4px; margin-bottom: 10px; }
  .owner-address { font-size: 16px; line-height: 1.4; }
  .owner-phone { display: flex; align-items: center; gap: 8px; font-weight: 700; font-size: 22px; margin-top: 2px; white-space: nowrap; }

  .social { position: absolute; top: 1104px; width: 58px; height: 58px; border-radius: 10px; }
  .social-one { left: 702px; background: linear-gradient(180deg, #c9b59a, #6b4f3a); }
  .social-two { left: 770px; background: #3b5a9a; }
</style>
</head>
<body>
<main class="flyer">
  <div class="hero-photo" role="img" aria-label="Young hunter in blaze orange cap and vest kneeling behind a large whitetail buck at night"></div>

  <div class="title-panel">
    <svg width="440" height="600" viewBox="0 0 440 600" aria-hidden="true">
      <path d="M0 0 H440 V595 C360 590 120 592 70 575 C20 555 0 520 0 480 Z" fill="var(--panel-grey)"/>
    </svg>
  </div>

  <span class="brand-mark" aria-hidden="true"></span>
  <div class="brand-name">HARLAN RIDGE</div>
  <div class="brand-sub">OUTFITTING</div>

  <h1 class="headline">
    <span class="year">2018</span>
    <span class="youth">Youth</span>
    <span class="firearm">Firearm</span>
    <span class="hunt">HUNT</span>
  </h1>

  <div class="contact-band">www.harlanridgeoutfitting.com | harlanridgeoutfitting@mailbox.com</div>

  <section class="details"></section>

  <div class="side-photo photo-trophy" role="img" aria-label="Hunter in the woods holding a trophy whitetail buck"></div>
  <div class="side-photo photo-interior" role="img" aria-label="Log cabin interior with kitchen, sofa and mounted deer heads"></div>
  <div class="side-photo photo-cabin" role="img" aria-label="Log-sided cabin with green metal roof on a grassy lawn"></div>

  <h2 class="event-date">October 6-8, 2018</h2>

  <ul class="package">
    <li><svg width="16" height="10" viewBox="0 0 16 10"><path d="M0 0 L7 5 L0 10 Z M8 0 L15 5 L8 10 Z" fill="var(--white)"/></svg>4 night stay in our private cabin that include<br>meals for 2 parents and the child</li>
    <li><svg width="16" height="10" viewBox="0 0 16 10"><path d="M0 0 L7 5 L0 10 Z M8 0 L15 5 L8 10 Z" fill="var(--white)"/></svg>Guided shotgun hunt on strictly managed properties</li>
    <li><svg width="16" height="10" viewBox="0 0 16 10"><path d="M0 0 L7 5 L0 10 Z M8 0 L15 5 L8 10 Z" fill="var(--white)"/></svg>Ground blinds in place</li>
    <li><svg width="16" height="10" viewBox="0 0 16 10"><path d="M0 0 L7 5 L0 10 Z M8 0 L15 5 L8 10 Z" fill="var(--white)"/></svg>Permit and license fees are the hunters responsibility</li>
  </ul>

  <div class="about">
    <p>Harlan Ridge Outfitting is a family owned and operated deer hunting outfitter located in Morgan and Scott Counties in west central Illinois. We provide low pressure, trophy whitetail hunts on privately owned farms across the region. The Harlans are lifelong residents and hunters of Morgan County, with the family farm being established well over 150 years ago.</p>
    <p>To go along with guiding deer and turkey hunters, we also offer a wide variety of professional hunting services that include whitetail land consulting, scouting services, CRP and food plot plantings and more.</p>
  </div>

  <address class="owner">
    <div class="owner-name">WADE HARLAN</div>
    <div class="owner-address">1480 Ridge Road<br>Millbrook, Illinois 62000</div>
    <div class="owner-phone">
      <svg width="22" height="22" viewBox="0 0 22 22" aria-hidden="true"><circle cx="11" cy="11" r="10" fill="none" stroke="var(--white)" stroke-width="1.5"/><path d="M7 6 C6 9 9 15 14 16 L15.5 14.5 L13.5 12.5 L12 13.5 C10.5 12.5 9.5 11.5 8.5 10 L9.5 8.5 L7.5 6.5 Z" fill="var(--white)"/></svg>
      (217)555-0142
    </div>
  </address>

  <div class="social social-one" role="img" aria-label="Photo sharing profile"></div>
  <div class="social social-two" role="img" aria-label="Social network profile"></div>
</main>
</body>
</html>
```